Harbor Nightclub

Nightclub flyer., digital single sided, for KV and PX. I included samples of some previous flyers we've used. Sample Info:
HARBOR
FRIDAYS
FRI MAY 1 2020
DJ VORTAN (club floor)
DJ RUZO & DJ TAV (residents on the lounge floor)
4217 Marlow Avenue Sacramento
www.harborvenuehall.example for list/VIP inquiries

Target Market(s)

Upscale top 40 crowd but want some cool and artsy like the examples included.

Font styles to use
Sans Serif

Requirements
Must have
• Harbor Logo
Nice to have
• Would be nice if the flyer can be incorporated later with DJ photos (sometimes we will add dj photos to pixagram etc). Would like a big city type of feel.
Should not have
• Nothing too sexual.

```html
<!DOCTYPE html>
<html lang="en">
<head>
<meta charset="utf-8">
<title>Harbor Fridays Flyer</title>
<link rel="stylesheet" href="https://fonts.googleapis.com/css2?family=Antonio:wght@100;200&family=Rajdhani:wght@500;600&display=swap">
<style>
  :root {
    --page: #ffffff;
    --ink: #07070c;
    --ember: #e0462a;
    --neon: #ff1a1a;
    --white: #ffffff;
  }
  html, body {
    margin: 0;
    width: 1200px;
    height: 1200px;
    overflow: hidden;
    background: var(--page);
  }
  .flyer {
    position: absolute;
    left: 219px;
    top: 61px;
    width: 761px;
    height: 1077px;
    overflow: hidden;
    background: var(--ink);
  }
  .flyer svg { display: block; }
  .headline { font-family: "Antonio", sans-serif; font-weight: 100; fill: var(--white); }
  .city-title { font-family: "Rajdhani", sans-serif; font-weight: 600; fill: var(--white); }
  .dj-name { font-family: "Antonio", sans-serif; font-weight: 200; fill: none; stroke: var(--ember); stroke-width: 2.2; filter: url(#softglow); }
  .detail { font-family: "Rajdhani", sans-serif; font-weight: 600; fill: var(--white); }
  .web { font-family: "Rajdhani", sans-serif; font-weight: 500; fill: var(--ember); }
  .brand-name { font-family: "Rajdhani", sans-serif; font-weight: 500; fill: var(--white); }
  .neon { fill: none; stroke: var(--neon); stroke-width: 3; filter: url(#glow); }
</style>
</head>
<body>
<div class="flyer">
  <svg width="761" height="1077" viewBox="0 0 761 1077" xmlns="http://www.w3.org/2000/svg">
    <defs>
      <linearGradient id="skyline" x1="0" y1="0" x2="0" y2="1">
        <stop offset="0" stop-color="#0d2350"/>
        <stop offset="0.28" stop-color="#1a2a55"/>
        <stop offset="0.45" stop-color="#12111c"/>
        <stop offset="1" stop-color="#0a0a14"/>
      </linearGradient>
      <linearGradient id="warm" x1="0" y1="0" x2="1" y2="0">
        <stop offset="0" stop-color="#ff3a1a" stop-opacity="0"/>
        <stop offset="0.5" stop-color="#ff5a20" stop-opacity="0.55"/>
        <stop offset="1" stop-color="#ff3a1a" stop-opacity="0"/>
      </linearGradient>
      <linearGradient id="cool" x1="0" y1="0" x2="1" y2="0">
        <stop offset="0" stop-color="#2b6bff" stop-opacity="0"/>
        <stop offset="0.5" stop-color="#3d7bff" stop-opacity="0.45"/>
        <stop offset="1" stop-color="#2b6bff" stop-opacity="0"/>
      </linearGradient>
      <linearGradient id="purple" x1="0" y1="0" x2="1" y2="0">
        <stop offset="0" stop-color="#5a48ff" stop-opacity="0"/>
        <stop offset="0.5" stop-color="#5a48ff" stop-opacity="0.5"/>
        <stop offset="1" stop-color="#5a48ff" stop-opacity="0"/>
      </linearGradient>
      <filter id="glow" x="-20%" y="-20%" width="140%" height="140%">
        <feGaussianBlur stdDeviation="3" result="b"/>
        <feMerge><feMergeNode in="b"/><feMergeNode in="SourceGraphic"/></feMerge>
      </filter>
      <filter id="softglow" x="-10%" y="-20%" width="120%" height="140%">
        <feGaussianBlur stdDeviation="2" result="b"/>
        <feMerge><feMergeNode in="b"/><feMergeNode in="SourceGraphic"/></feMerge>
      </filter>
    </defs>

    <rect class="backdrop" width="761" height="1077" fill="url(#skyline)" role="img" aria-label="Night photo of a city bridge skyline fading into a crowd outside the club"/>

    <g class="light-streaks" transform="rotate(-38 380 540)">
      <rect x="-300" y="330" width="1300" height="10" fill="url(#cool)"/>
      <rect x="-300" y="250" width="1300" height="4" fill="url(#cool)"/>
      <rect x="-300" y="470" width="1300" height="22" fill="url(#warm)"/>
      <rect x="-300" y="540" width="1300" height="8" fill="url(#warm)"/>
      <rect x="-300" y="610" width="1300" height="30" fill="url(#warm)"/>
      <rect x="-300" y="690" width="1300" height="6" fill="url(#warm)"/>
      <rect x="-300" y="800" width="1300" height="14" fill="url(#purple)"/>
      <rect x="-300" y="880" width="1300" height="26" fill="url(#purple)"/>
      <rect x="-300" y="960" width="1300" height="6" fill="url(#cool)"/>
    </g>

    <g class="neon-frame">
      <polyline class="neon" points="181,70 647,165 578,469"/>
      <line class="neon" x1="181" y1="70" x2="578" y2="469" stroke-dasharray="90 14 60 20"/>
      <polyline class="neon" points="0,889 78,975 0,1000"/>
      <polyline class="neon" points="0,930 118,1035 0,1020"/>
      <line class="neon" x1="0" y1="970" x2="128" y2="1051"/>
    </g>

    <text class="city-title" x="200" y="274" font-size="48" textLength="390" lengthAdjust="spacing">HARBOR</text>
    <text class="headline" x="200" y="454" font-size="180" textLength="363" lengthAdjust="spacingAndGlyphs">FRIDAYS</text>
    <text class="detail" x="373" y="493" text-anchor="middle" font-size="26" textLength="173" lengthAdjust="spacing">FRI MAY 1 2020</text>

    <text class="dj-name" x="247" y="625" font-size="76" textLength="274" lengthAdjust="spacingAndGlyphs">DJ VORTAN</text>
    <text class="detail" x="384" y="660" text-anchor="middle" font-size="26" textLength="119" lengthAdjust="spacing">CLUB FLOOR</text>

    <text class="dj-name" x="200" y="777" font-size="76" textLength="362" lengthAdjust="spacingAndGlyphs">DJ RUZO &amp; DJ TAV</text>
    <text class="detail" x="381" y="813" text-anchor="middle" font-size="26" textLength="341" lengthAdjust="spacing">RESIDENTS ON THE LOUNGE FLOOR</text>

    <g class="brand">
      <circle cx="381" cy="889" r="18" fill="none" stroke="#ffffff" stroke-width="2.5"/>
      <text class="brand-name" x="381" y="928" text-anchor="middle" font-size="19" textLength="82" lengthAdjust="spacing">HARBOR</text>
    </g>

    <text class="detail" x="381" y="966" text-anchor="middle" font-size="26" textLength="362" lengthAdjust="spacing">4217 MARLOW AVENUE SACRAMENTO</text>
    <text class="web" x="382" y="1002" text-anchor="middle" font-size="24" textLength="505" lengthAdjust="spacing">WWW.HARBORVENUEHALL.EXAMPLE</text>
    <text class="detail" x="381" y="1034" text-anchor="middle" font-size="22" textLength="219" lengthAdjust="spacing">FOR LIST/VIP INQUIRIES</text>
  </svg>
</div>
</body>
</html>
```